'Ormel Property Development' Business Card

Business Card Features:

High Quality (potentially textured) thick card - preference is white textured card

Logo (supplied)

We plan to use the vertical logo as the main logo. But i am happy for people to use either if they find it works better for the design of the card.

The building icon and also the insert to the 'E' is in a metallic finish, i think this should be finished in a metallic embossed or raised style.
Updates

Please note i have attached both a horizontal and Vertical Logo for your reference. We plan to use the vertical logo as the main logo. But i am happy for people to use either if they find it works better for the design of the card.

Please note i am considering having the cards made on stainless steel. This introduces the option of having cut outs in the card and etching or printing for the design. If you have a good concept for this please submit.

http://www.tinquarry.example/black-metal-cards# this is a site that makes the metal cards to offer some direction . . . . Please note i am basic the selection o the best design, if that means normal print cards on paper then this is what i will choose. But there are some great options with the metal. Thanks.

Industry/Entity Type

Building

Requirements
Must have
• Helvetica font to details side of card - logo as supplied to opposite side.

Card Details:

Darrow Pketts
Managing Director

+61 487 263 518
+61 3 6172 4809

PO Box 73
Bentleigh, VIC 3024

darrow@ormel.example

www.ormel.example

```html
<!DOCTYPE html>
<html lang="en">
<head>
<meta charset="utf-8">
<title>Ormel Property Development – Business Card</title>
<link href="https://fonts.googleapis.com/css2?family=Arimo:wght@400;700&display=swap" rel="stylesheet">
<style>
  :root {
    --page-bg: #ffffff;
    --metal-dark: #16191a;
    --metal-mid: #2b3031;
    --metal-light: #6e7677;
    --ink-light: #ffffff;
    --ink-soft: #e3e6e6;
    --ink-note: #111111;
    --perforation-light: #d9dcdc;
  }
  html, body {
    margin: 0;
    padding: 0;
    width: 1200px;
    height: 1000px;
    overflow: hidden;
    background: var(--page-bg);
    font-family: "Arimo", Helvetica, Arial, sans-serif;
  }
  .stage {
    position: relative;
    width: 1200px;
    height: 1000px;
  }
  .metal-card {
    position: absolute;
    left: 160px;
    top: 190px;
    width: 880px;
    height: 556px;
    border-radius: 34px;
    overflow: hidden;
    background:
      linear-gradient(90deg,
        var(--metal-dark) 0%,
        var(--metal-mid) 40%,
        var(--metal-dark) 50%,
        var(--metal-light) 64%,
        var(--metal-mid) 74%,
        var(--metal-dark) 88%,
        var(--metal-mid) 100%);
  }
  .perforation-field {
    position: absolute;
    left: 0;
    top: 0;
    width: 460px;
    height: 556px;
    background:
      radial-gradient(ellipse 70% 80% at 30% 45%, rgba(217,220,220,0.55) 0%, rgba(217,220,220,0.35) 55%, rgba(217,220,220,0) 100%);
  }
  .brand-mark {
    position: absolute;
    left: 40px;
    top: 300px;
    width: 320px;
    text-align: center;
    color: var(--ink-light);
  }
  .brand-name {
    font-weight: 700;
    font-size: 74px;
    letter-spacing: 4px;
    line-height: 1;
  }
  .brand-tagline {
    margin-top: 10px;
    font-weight: 400;
    font-size: 19px;
    letter-spacing: 0.5px;
    color: var(--ink-light);
  }
  .holder {
    position: absolute;
    right: 46px;
    top: 44px;
    text-align: right;
    color: var(--ink-light);
  }
  .holder-name {
    font-weight: 700;
    font-size: 27px;
    line-height: 1.1;
  }
  .holder-role {
    font-weight: 700;
    font-size: 14px;
    margin-right: 26px;
    color: var(--ink-soft);
  }
  .contact-list {
    position: absolute;
    left: 450px;
    top: 352px;
    margin: 0;
    padding: 0;
    list-style: none;
    color: var(--ink-light);
    font-weight: 700;
    font-size: 21px;
  }
  .contact-list li {
    display: flex;
    align-items: center;
    height: 38px;
  }
  .contact-icon {
    width: 18px;
    height: 18px;
    margin-right: 10px;
    fill: var(--ink-light);
    flex: none;
  }
  .production-note {
    position: absolute;
    left: 0;
    width: 1200px;
    top: 775px;
    text-align: center;
    font-weight: 700;
    font-size: 20px;
    color: var(--ink-note);
  }
</style>
</head>
<body>
<main class="stage">
  <section class="metal-card" aria-label="Ormel Property Development business card">
    <div class="perforation-field" role="img" aria-label="Field of round perforations cut through the metal card"></div>

    <div class="brand-mark">
      <div class="brand-name">ORMEL</div>
      <div class="brand-tagline">Property Development</div>
    </div>

    <div class="holder">
      <div class="holder-name">Darrow Pketts</div>
      <div class="holder-role">Managing Director</div>
    </div>

    <ul class="contact-list">
      <li>
        <svg class="contact-icon" viewBox="0 0 24 24" aria-hidden="true"><path d="M6.6 10.8a15.1 15.1 0 0 0 6.6 6.6l2.2-2.2c.3-.3.7-.4 1-.2 1.1.4 2.3.6 3.6.6.6 0 1 .4 1 1V20c0 .6-.4 1-1 1A17 17 0 0 1 3 4c0-.6.4-1 1-1h3.5c.6 0 1 .4 1 1 0 1.3.2 2.5.6 3.6.1.3 0 .7-.2 1z"/></svg>
        0487263518
      </li>
      <li>
        <svg class="contact-icon" viewBox="0 0 24 24" aria-hidden="true"><path d="M8 2h8a1.5 1.5 0 0 1 1.5 1.5v17A1.5 1.5 0 0 1 16 22H8a1.5 1.5 0 0 1-1.5-1.5v-17A1.5 1.5 0 0 1 8 2zm0 3v12h8V5zm4 13.5a1 1 0 1 0 0 2 1 1 0 0 0 0-2z"/></svg>
        1800 640 275
      </li>
      <li>
        <svg class="contact-icon" viewBox="0 0 24 24" aria-hidden="true"><path d="M2 5h20v14H2zm2 2v.4l8 5.2 8-5.2V7zm0 2.8V17h16V9.8l-8 5.2z"/></svg>
        darrow@ormel.example
      </li>
      <li>
        <svg class="contact-icon" viewBox="0 0 24 24" aria-hidden="true"><path d="M12 2a10 10 0 1 0 0 20 10 10 0 0 0 0-20zm6.9 6h-3a15 15 0 0 0-1.3-3.9A8 8 0 0 1 18.9 8zM12 4c.8 1.2 1.5 2.5 1.9 4h-3.8c.4-1.5 1.1-2.8 1.9-4zM4.3 14a8 8 0 0 1 0-4h3.4a16 16 0 0 0 0 4zm.8 2h3a15 15 0 0 0 1.3 3.9A8 8 0 0 1 5.1 16zm3-8h-3a8 8 0 0 1 4.3-3.9A15 15 0 0 0 8.1 8zM12 20c-.8-1.2-1.5-2.5-1.9-4h3.8c-.4 1.5-1.1 2.8-1.9 4zm2.3-6H9.7a14 14 0 0 1 0-4h4.6a14 14 0 0 1 0 4zm.3 5.9a15 15 0 0 0 1.3-3.9h3a8 8 0 0 1-4.3 3.9zm1.7-5.9a16 16 0 0 0 0-4h3.4a8 8 0 0 1 0 4z"/></svg>
        www.ormel.example
      </li>
      <li>
        <svg class="contact-icon" viewBox="0 0 24 24" aria-hidden="true"><path d="M12 3 2 12h3v8h5v-5h4v5h5v-8h3z"/></svg>
        PO BOX 73 Bentleigh, VIC 3024
      </li>
    </ul>
  </section>

  <p class="production-note">Note: Only the dots and the logo in the business card will be cut off.</p>
</main>
</body>
</html>
```